Strong, modern, clean Business Card design

Looking for a stunning, but CLEAN business card design. While we are a faith-based organization, we do NOT want this to look religious.

Industry/Entity Type

Non-Profit

Contact Information for Business Card

Mark Dalton | Lead Pastor
mark@BraverHollow.org
555-218-9034
PO Box 7183
Fairmont, CO 80817

Font styles to use
Serif
Sans Serif

Requirements
Should not have
• Religious imagery or symbolism

```html
<!DOCTYPE html>
<html lang="en">
<head>
<meta charset="utf-8">
<title>Mark Dalton – Business Card</title>
<link rel="stylesheet" href="https://fonts.googleapis.com/css2?family=Merriweather:wght@400;700&display=swap">
<style>
  :root {
    --card-black: #020101;
    --gold: #c4992f;
    --band-red: #5c1016;
    --band-red-light: #741a20;
    --edge-dark: #1e0709;
  }
  html, body {
    margin: 0;
    padding: 0;
    overflow: hidden;
    background: var(--card-black);
  }
  .card {
    position: relative;
    width: 1200px;
    height: 681px;
    background: var(--card-black);
    overflow: hidden;
    font-family: "Merriweather", Georgia, serif;
    color: var(--gold);
  }
  .side-band {
    position: absolute;
    top: 0;
    height: 100%;
    background: linear-gradient(135deg, var(--band-red) 0%, var(--band-red-light) 50%, var(--band-red) 100%);
  }
  .side-band--left { left: 0; width: 167px; }
  .side-band--right { left: 1043px; width: 157px; }
  .band-edge {
    position: absolute;
    top: 0;
    width: 6px;
    height: 100%;
    background: var(--edge-dark);
    border-left: 1px solid #3a0d11;
    border-right: 1px solid #3a0d11;
  }
  .band-edge--left { left: 170px; }
  .band-edge--right { left: 1030px; }
  .org-name {
    position: absolute;
    top: 74px;
    left: 0;
    width: 100%;
    text-align: center;
    font-size: 34px;
    font-weight: 400;
    letter-spacing: 0.06em;
  }
  .person-name {
    position: absolute;
    top: 218px;
    left: 0;
    width: 100%;
    text-align: center;
    font-size: 44px;
    font-weight: 700;
    letter-spacing: 0.3em;
    text-transform: uppercase;
    margin: 0;
  }
  .person-title {
    position: absolute;
    top: 280px;
    left: 0;
    width: 100%;
    text-align: center;
    font-size: 26px;
    font-weight: 700;
    letter-spacing: 0.36em;
    text-transform: uppercase;
    margin: 0;
  }
  .contact {
    position: absolute;
    top: 488px;
    left: 0;
    width: 100%;
    text-align: center;
    list-style: none;
    margin: 0;
    padding: 0;
  }
  .contact li {
    font-size: 26px;
    font-weight: 700;
    letter-spacing: 0.35em;
    text-transform: uppercase;
    line-height: 46.5px;
  }
</style>
</head>
<body>
  <div class="card">
    <div class="side-band side-band--left" role="img" aria-label="Deep red chevron pattern band"></div>
    <div class="side-band side-band--right" role="img" aria-label="Deep red chevron pattern band"></div>
    <div class="band-edge band-edge--left"></div>
    <div class="band-edge band-edge--right"></div>

    <div class="org-name">Braver Hollow</div>

    <h1 class="person-name">Mark Dalton</h1>
    <p class="person-title">Lead Pastor</p>

    <ul class="contact">
      <li>mark@BraverHollow.org</li>
      <li>555-218-9034</li>
      <li>PO Box 7183</li>
      <li>Fairmont, CO 80817</li>
    </ul>
  </div>
</body>
</html>
```